Marrowby's Vacation Rentals Business Card

Multi Million dollar villa rentals in the Dominican Republic.

Industry/Entity Type

Business

Contact Information for Business Card

I am looking for a high-end look around my company name/logo (see attached) on one side incorporating the following info: first and last name, title, address, phone #, email and company website. On the backside I want to add a full color picture of one of our villas (see attached).

```html
<!DOCTYPE html>
<html lang="en">
<head>
<meta charset="utf-8">
<title>Marrowby's Vacation Rentals – Business Card</title>
<link href="https://fonts.googleapis.com/css2?family=Arimo:wght@400;700&display=swap" rel="stylesheet">
<style>
  :root {
    --backdrop: #2b2b2b;
    --card-white: #f6f6f6;
    --card-shade: #e4e4e4;
    --accent: #e8743b;
    --ink: #2a2a2a;
    --muted: #555555;
    --sky: #3f7fc8;
    --pool: #2aa6d6;
    --villa: #e9e4dc;
  }
  * { box-sizing: border-box; margin: 0; padding: 0; }
  html, body {
    width: 1200px; height: 997px; overflow: hidden;
    background: var(--backdrop);
    font-family: "Arimo", Arial, sans-serif;
  }
  .canvas { position: relative; width: 1200px; height: 997px; }

  .card {
    position: absolute; left: 250px; width: 700px; height: 400px;
    border-radius: 22px; overflow: hidden;
    box-shadow: 0 14px 30px rgba(0,0,0,.55);
  }
  .card--front { top: 66px; background: linear-gradient(160deg, #ffffff 0%, var(--card-white) 55%, var(--card-shade) 100%); }
  .card--back { top: 530px; }

  .brand-name {
    color: var(--ink);
    font-family: "Arimo", Arial, sans-serif;
    font-weight: 400;
    white-space: nowrap;
  }
  .card--front .brand-name { position: absolute; left: 46px; top: 56px; font-size: 34px; }

  .office { position: absolute; right: 46px; top: 128px; text-align: right; }
  .office__name { color: var(--accent); font-weight: 700; font-size: 15px; letter-spacing: .5px; }
  .office__line { color: var(--muted); font-size: 14px; margin-top: 3px; }

  .divider { position: absolute; left: 46px; right: 46px; top: 206px; height: 2px; background: var(--accent); }

  .person { position: absolute; left: 46px; top: 224px; }
  .person__name { color: var(--accent); font-weight: 700; font-size: 19px; letter-spacing: 1px; text-transform: uppercase; }
  .person__role { color: var(--muted); font-size: 14px; margin-top: 3px; }

  .contact { position: absolute; left: 46px; bottom: 40px; list-style: none; }
  .contact__item { display: flex; align-items: center; gap: 10px; color: var(--muted); font-size: 15px; margin-top: 10px; }
  .contact__icon { width: 20px; height: 20px; flex: none; }

  .villa-photo {
    position: absolute; inset: 0;
    background: linear-gradient(180deg, var(--sky) 0%, #8fb7e0 18%, var(--villa) 30%, #d8d0c4 62%, var(--pool) 78%, #1e7fb0 100%);
  }
  .back-badge {
    position: absolute; right: 24px; bottom: 130px;
    background: rgba(255,255,255,.82); border-radius: 8px; padding: 12px 18px;
  }
  .back-badge .brand-name { font-size: 24px; }
</style>
</head>
<body>
<main class="canvas">

  <section class="card card--front" aria-label="Business card front">
    <p class="brand-name">Marrowby's Vacation Rentals</p>

    <div class="office">
      <p class="office__name">MARROWBY'S VACATION RENTALS</p>
      <p class="office__line">418 Harbor Crest Lane, Oakmont</p>
      <p class="office__line">CA 92614</p>
    </div>

    <div class="divider"></div>

    <div class="person">
      <p class="person__name">Daniel Hartwell</p>
      <p class="person__role">Director</p>
    </div>

    <ul class="contact">
      <li class="contact__item">
        <svg class="contact__icon" viewBox="0 0 20 20" aria-hidden="true">
          <circle cx="10" cy="10" r="10" fill="var(--accent)"/>
          <path d="M6 7.5c0-1 1-1.5 1.6-1.5l1 2-1 1c.5 1.2 1.4 2.1 2.6 2.6l1-1 2 1c0 .6-.5 1.6-1.5 1.6C8.6 13.2 6 10.6 6 7.5z" fill="#fff"/>
        </svg>
        0417 583 926
      </li>
      <li class="contact__item">
        <svg class="contact__icon" viewBox="0 0 20 20" aria-hidden="true">
          <circle cx="10" cy="10" r="10" fill="var(--accent)"/>
          <rect x="5" y="6.5" width="10" height="7" rx="1" fill="#fff"/>
          <path d="M5.5 7l4.5 3.5L14.5 7" stroke="var(--accent)" stroke-width="1.2" fill="none"/>
        </svg>
        danhartwell@maplecrestvillas.com
      </li>
    </ul>
  </section>

  <section class="card card--back" aria-label="Business card back">
    <div class="villa-photo" role="img" aria-label="Photograph of a white two-storey villa with arched terrace, red tile roof, blue loungers and a swimming pool"></div>
    <div class="back-badge">
      <p class="brand-name">Marrowby's Vacation Rentals</p>
    </div>
  </section>

</main>
</body>
</html>
```